RW dental business card. A family dental practice.

Logo plus the following details.

RW Dental
Dr. Marcus Ellory D.D.S
Family. Implant.Cosmetic

48 Fernbrook Lane, Unit 12-13
Markham, ON K2P7R4

Tel: 905-318-2670
Fx:905-318-9025
rwdental-sample.ca

On the double side:

Next app: ______________________

Please notify us at least 48hours in advance to avoid cancellation fees.

Target Market(s)

Family Dental Services

Industry/Entity Type

Dental

Contact Information for Business Card

Put logo prominently and all the info along with it.

Font styles to use
Other font styles liked:
• See Logo Font

Colors
0255a3
3277b5
85acd3
00a990
33b8a4

Requirements
Must have
• Logo and the info stated above.
• See the logo color scheme.
• Or a grayscale (Black, white gray) combination
Nice to have
• A modern unique layout
Should not have
• too simple a design

```html
<!DOCTYPE html>
<html lang="en">
<head>
<meta charset="UTF-8">
<title>RW Dental – Business Card</title>
<link rel="stylesheet" href="https://fonts.googleapis.com/css2?family=Source+Sans+3:wght@400;600;700&display=swap">
<style>
  :root {
    --navy: #0f3f7a;
    --blue: #0255a3;
    --teal: #00a990;
    --teal-soft: #33b8a4;
    --ink: #2b2b2b;
    --paper: #ffffff;
    --stage: #e6e6e6;
  }
  * { box-sizing: border-box; margin: 0; padding: 0; }
  html, body {
    width: 1200px; height: 844px; overflow: hidden;
    background: var(--stage);
    font-family: "Source Sans 3", "Myriad Pro", Arial, sans-serif;
  }
  .canvas {
    position: relative; width: 1200px; height: 844px;
    display: flex; align-items: center; justify-content: center; gap: 40px;
  }
  .card {
    position: relative; width: 520px; height: 298px;
    background: var(--paper); overflow: hidden;
    box-shadow: 0 6px 18px rgba(0,0,0,0.18);
  }

  /* Front */
  .brand {
    position: absolute; left: 46px; top: 40px;
    display: flex; align-items: center; gap: 16px;
  }
  .brand-mark {
    width: 56px; height: 56px; border-radius: 50%;
    border: 4px solid var(--teal);
  }
  .brand-name {
    font-size: 44px; font-weight: 400; line-height: 1; color: var(--teal);
  }
  .brand-tagline {
    font-size: 19px; color: var(--navy); margin-top: 2px;
  }
  .doctor {
    position: absolute; left: 46px; top: 138px;
  }
  .doctor-name { font-size: 22px; font-weight: 700; color: var(--navy); }
  .doctor-services { font-size: 16px; color: var(--teal); margin-top: -2px; }
  .contact-list {
    position: absolute; left: 46px; top: 196px; list-style: none;
    font-size: 15px; line-height: 19px; color: var(--ink);
  }
  .contact-list li { display: flex; align-items: center; gap: 7px; }
  .contact-list svg { width: 11px; height: 11px; fill: var(--navy); }
  .contact-web { color: var(--teal); }
  .address {
    position: absolute; left: 46px; bottom: 22px;
    font-size: 15px; color: var(--ink);
  }

  /* Back */
  .corner-disc {
    position: absolute; right: -90px; top: -120px;
    width: 260px; height: 260px; border-radius: 50%;
    background: var(--teal-soft); opacity: 0.9;
  }
  .appointment {
    position: absolute; left: 48px; top: 116px; width: 260px;
  }
  .appointment-label {
    font-size: 19px; font-weight: 700; color: var(--teal); letter-spacing: 0.3px;
  }
  .appointment-line {
    margin-top: 34px; border-top: 1px solid #9a9a9a; width: 220px;
  }
  .notice {
    position: absolute; left: 48px; top: 214px; width: 260px;
    font-size: 13px; line-height: 16px; color: var(--navy);
  }
</style>
</head>
<body>
<main class="canvas">

  <section class="card card-front" aria-label="Business card front">
    <div class="brand">
      <span class="brand-mark" aria-hidden="true"></span>
      <div>
        <div class="brand-name">RW Dental</div>
        <div class="brand-tagline">Your dental health support Team</div>
      </div>
    </div>

    <div class="doctor">
      <div class="doctor-name">Dr. Marcus Ellory D.D.S</div>
      <div class="doctor-services">Family. Implant. Cosmetic</div>
    </div>

    <ul class="contact-list">
      <li>
        <svg viewBox="0 0 24 24" aria-hidden="true"><path d="M6.6 10.8a15 15 0 0 0 6.6 6.6l2.2-2.2c.3-.3.7-.4 1-.2 1.1.4 2.3.6 3.6.6.6 0 1 .4 1 1V20c0 .6-.4 1-1 1A17 17 0 0 1 3 4c0-.6.4-1 1-1h3.5c.6 0 1 .4 1 1 0 1.3.2 2.5.6 3.6.1.3 0 .7-.2 1z"/></svg>
        905-318-2670
      </li>
      <li>
        <svg viewBox="0 0 24 24" aria-hidden="true"><path d="M6 3h10v5H6zM3 9h18v10h-3v3H6v-3H3zm5 7v4h8v-4z"/></svg>
        905-318-9025
      </li>
      <li class="contact-web">
        <svg viewBox="0 0 24 24" aria-hidden="true"><circle cx="12" cy="12" r="10"/></svg>
        www.rwdental-sample.ca
      </li>
    </ul>

    <p class="address">48 Fernbrook Lane, Unit 12-13 Markham,ON K2P7R4</p>
  </section>

  <section class="card card-back" aria-label="Business card back">
    <span class="corner-disc" aria-hidden="true"></span>
    <div class="appointment">
      <div class="appointment-label">NEXT APPOINTMENT</div>
      <div class="appointment-line"></div>
    </div>
    <p class="notice">Please notify us at least 48hours in advance to avoid cancellation fees.</p>
  </section>

</main>
</body>
</html>
```